Thornwick Estates Managment Ltd website

Need a website To inform people/clients of the services we provide. 5 pages total with a local feel. Bristol, UK. I have logo artwork already is like the look based on
incorporate the artwork attached for theme, feel and colours fonts info etc

To best describe the business have a brief look at www.fernbaylettings.co.uk which is a local firm offering the same services. This is for your ref only and not to be copied.

Target Market(s)

Property Investors/Landlords

Coding

Coded - Design and coding required

Number of Pages Required

5+ page

Colors
0392cd
f68d4d

Requirements
Must have
• local feel. Possibly using some local architecture or historic landmarks etc. This is fexible.
• most also be mobile device compatible
Nice to have
• the membership logos - files attached: KTB, GHW, DVT and safebondhold.co.uk

```html
<!DOCTYPE html>
<html lang="en">
<head>
<meta charset="utf-8">
<title>Thornwick Estates Managment Ltd</title>
<link rel="stylesheet" href="https://fonts.googleapis.com/css2?family=Roboto+Slab:wght@400;600;700&family=Open+Sans:wght@400;600&display=swap">
<style>
:root{
  --teal:#1d4b5c;
  --teal-line:#2d5466;
  --orange:#f39a2b;
  --ink:#2a2a2a;
  --muted:#6b6b6b;
  --nav:#2b2b2b;
  --footer:#333436;
  --bottom:#1e1f20;
  --white:#ffffff;
}
*{margin:0;padding:0;box-sizing:border-box}
html,body{width:1200px;height:2908px;overflow:hidden}
body{position:relative;background:var(--white);font-family:"Open Sans",Arial,sans-serif;color:var(--muted)}
.abs{position:absolute}
.slab{font-family:"Roboto Slab",Georgia,serif}

/* header */
.brand{left:132px;top:30px;display:flex;align-items:center;gap:14px}
.brand-mark{width:54px;height:54px;background:var(--teal)}
.brand-name{font-family:"Roboto Slab",Georgia,serif;font-weight:600;color:var(--teal);font-size:34px;line-height:34px}
.brand-name small{display:block;font-size:15px;line-height:18px}
.contact-item{top:40px;display:flex;align-items:center;gap:14px}
.contact-item svg{width:30px;height:30px}
.contact-label{font-size:13px;color:var(--muted);line-height:18px}
.contact-value{font-size:16px;font-weight:600;color:var(--ink);line-height:22px}

/* nav */
.nav{left:0;top:120px;width:1200px;height:52px;background:var(--nav);display:flex;justify-content:center;align-items:center;gap:0}
.nav a{font-family:"Roboto Slab",Georgia,serif;font-size:12px;color:#9fb6c6;text-decoration:none;text-transform:uppercase;padding:0 29px;letter-spacing:.3px}
.nav a.active{color:var(--orange)}
.nav a.active::before{content:"";display:inline-block;width:6px;height:6px;border-radius:50%;background:var(--orange);margin-right:8px;vertical-align:middle}

/* hero */
.hero{left:0;top:172px;width:1200px;height:520px;background:linear-gradient(180deg,#1d3a6e 0%,#3b6aa8 40%,#6a86b3 52%,#23406b 62%,#172d4d 100%)}
.hero-title{left:0;top:328px;width:1200px;text-align:center;color:var(--white);font-family:"Roboto Slab",Georgia,serif;font-weight:700;font-size:37px;line-height:54px;text-shadow:0 2px 4px rgba(0,0,0,.35)}
.hero-btn{left:522px;top:474px;width:174px;height:56px;background:var(--teal);color:var(--white);font-size:19px;display:flex;align-items:center;justify-content:center;gap:10px}
.dots{left:584px;top:566px;display:flex;gap:8px}
.dots span{width:12px;height:12px;border-radius:50%;background:var(--white)}
.dots span:first-child{background:var(--orange)}

/* section headings */
.heading{border-left:4px solid var(--orange);padding-left:14px;font-family:"Roboto Slab",Georgia,serif;color:var(--teal);line-height:30px}
.heading .lead{font-size:22px;color:var(--ink);display:block}
.heading .main{font-size:23px;text-transform:uppercase;letter-spacing:.6px;display:block}
.copy{font-size:12px;line-height:22px;color:var(--muted)}
.btn{height:40px;background:var(--teal);color:var(--white);font-size:11px;text-transform:uppercase;display:flex;align-items:center;justify-content:center;gap:8px}
.btn svg,.hero-btn svg{width:14px;height:14px}

/* feature blocks */
.photo{position:absolute}
.panel{background:var(--white)}
.rule{position:absolute;height:3px;background:var(--teal-line)}
.vrule{position:absolute;width:3px;background:var(--teal-line)}

/* gallery */
.tile{position:absolute;width:287px;height:254px}
.view-all{left:990px;top:1665px;font-family:"Roboto Slab",Georgia,serif;font-size:15px;color:var(--teal);display:flex;align-items:center;gap:8px}

/* membership */
.member{position:absolute;top:2418px;width:222px;height:95px;border:2px solid var(--teal-line);display:flex;align-items:center;justify-content:center}
.member-badge{width:120px;height:50px;background:#d9dde0}

/* footer */
.map{left:0;top:2568px;width:1200px;height:280px;background:linear-gradient(135deg,#3a3b3d,#2e2f31)}
.contact-card{left:320px;top:2598px;width:560px;height:190px;background:rgba(20,20,20,.55);display:flex;flex-direction:column;align-items:center;justify-content:center;gap:10px;color:var(--white);font-size:18px}
.contact-card div{display:flex;align-items:center;gap:10px}
.contact-card svg{width:18px;height:18px}
.bottom{left:0;top:2848px;width:1200px;height:60px;background:var(--bottom)}
.copyright{left:132px;top:2870px;font-size:12px;color:#c8c8c8}
.social{top:2860px;display:flex;gap:8px;left:912px}
.social span{width:34px;height:34px;background:var(--orange)}
</style>
</head>
<body>

<header>
  <div class="abs brand">
    <span class="brand-mark"></span>
    <div class="brand-name">Thornwick<small>estates management ltd</small></div>
  </div>
  <div class="abs contact-item" style="left:606px">
    <svg viewBox="0 0 30 30"><circle cx="15" cy="15" r="13" fill="none" stroke="#f39a2b" stroke-width="2"/><rect x="8" y="10" width="14" height="10" fill="#f39a2b"/><path d="M8 10l7 6 7-6" fill="none" stroke="#fff" stroke-width="1.5"/></svg>
    <div><div class="contact-label">Email us</div><div class="contact-value">info@thornwickestates.co.uk</div></div>
  </div>
  <div class="abs contact-item" style="left:908px">
    <svg viewBox="0 0 30 30"><circle cx="15" cy="15" r="13" fill="none" stroke="#2d5466" stroke-width="2"/><path d="M10 8c-2 2-1 6 3 10s8 5 10 3l-3-3-2 2c-2-1-4-3-5-5l2-2z" fill="#2d5466"/></svg>
    <div><div class="contact-label">Call us now on</div><div class="contact-value">011-555-01427</div></div>
  </div>
</header>

<nav class="abs nav">
  <a class="active">Home</a><a>Landlords</a><a>Agencies</a><a>About us</a><a>Gallery</a><a>Our membership</a><a>Contact</a>
</nav>

<section>
  <div class="abs hero" role="img" aria-label="City waterfront skyline at dusk with lit towers reflected in the harbour"></div>
  <h1 class="abs hero-title">Welcome to<br>Thornwick Estates Managements</h1>
  <div class="abs hero-btn">About us <svg viewBox="0 0 14 14"><circle cx="7" cy="7" r="7" fill="#fff"/><path d="M5.5 4l3 3-3 3" fill="none" stroke="#1d4b5c" stroke-width="2"/></svg></div>
  <div class="abs dots"><span></span><span></span><span></span></div>
</section>

<section>
  <h2 class="abs heading" style="left:132px;top:712px"><span class="lead">Welcome to</span><span class="main">Thornwick Estates Managements</span></h2>
  <p class="abs copy" style="left:132px;top:788px;width:936px">We look after homes across Bristol for landlords who want steady rent, cared for property and tenants who stay. Our local team handles viewings, checks, repairs and legal paperwork so you never need to chase a thing. From Clifton flats to Old Market terraces we know every street, every agent and every rule that matters to your letting business and your peace of mind.</p>
  <div class="abs btn" style="left:132px;top:873px;width:136px">Read more <svg viewBox="0 0 14 14"><circle cx="7" cy="7" r="7" fill="#fff"/><path d="M5.5 4l3 3-3 3" fill="none" stroke="#1d4b5c" stroke-width="2"/></svg></div>
</section>

<section>
  <div class="photo" style="left:132px;top:945px;width:483px;height:317px;background:linear-gradient(180deg,#1d2d5c 0%,#3a4a7a 45%,#b08a5a 75%,#6a5a4a 100%)" role="img" aria-label="Historic square at night with a lit palazzo and a stone fountain"></div>
  <div class="abs panel" style="left:582px;top:975px;width:240px;height:257px"></div>
  <div class="rule" style="left:582px;top:975px;width:240px"></div>
  <div class="rule" style="left:582px;top:1229px;width:240px"></div>
  <div class="vrule" style="left:582px;top:975px;height:257px"></div>
  <h2 class="abs heading" style="left:612px;top:1002px"><span class="lead">For</span><span class="main">Landlords</span></h2>
  <p class="abs copy" style="left:602px;top:1070px;width:466px">Full management or tenant find only, we match the service to your needs. We vet every applicant, hold deposits in a protected scheme and keep you informed at every step of the tenancy.</p>
  <div class="abs btn" style="left:602px;top:1175px;width:136px">Read more <svg viewBox="0 0 14 14"><circle cx="7" cy="7" r="7" fill="#fff"/><path d="M5.5 4l3 3-3 3" fill="none" stroke="#1d4b5c" stroke-width="2"/></svg></div>
</section>

<section>
  <div class="photo" style="left:585px;top:1285px;width:483px;height:317px;background:linear-gradient(180deg,#5a7aa8 0%,#9aaec8 35%,#b88a5a 60%,#6a5a3a 100%)" role="img" aria-label="Ancient ruins with tall stone columns under a cloudy sky"></div>
  <div class="rule" style="left:375px;top:1315px;width:242px"></div>
  <div class="rule" style="left:375px;top:1569px;width:242px"></div>
  <div class="vrule" style="left:614px;top:1315px;height:257px"></div>
  <h2 class="abs heading" style="left:132px;top:1340px"><span class="lead">For</span><span class="main">Tenants</span></h2>
  <p class="abs copy" style="left:132px;top:1410px;width:460px">Looking for a home in Bristol? Browse our current lets, book a viewing online and meet a friendly local team who answer quickly and fix problems fast. Good homes, fair terms and clear contracts.</p>
  <div class="abs btn" style="left:132px;top:1515px;width:136px">Read more <svg viewBox="0 0 14 14"><circle cx="7" cy="7" r="7" fill="#fff"/><path d="M5.5 4l3 3-3 3" fill="none" stroke="#1d4b5c" stroke-width="2"/></svg></div>
</section>

<section>
  <h2 class="abs heading" style="left:132px;top:1652px"><span class="lead">Our</span><span class="main">Gallery</span></h2>
  <div class="abs view-all">View all <svg viewBox="0 0 14 14" width="14" height="14"><circle cx="7" cy="7" r="7" fill="#1d4b5c"/><path d="M5.5 4l3 3-3 3" fill="none" stroke="#fff" stroke-width="2"/></svg></div>
  <div class="tile" style="left:132px;top:1740px;background:linear-gradient(180deg,#26282e,#3a3530)" role="img" aria-label="Theatre facade at night"></div>
  <svg class="abs" style="left:258px;top:1855px" width="32" height="32" viewBox="0 0 32 32"><circle cx="13" cy="13" r="8" fill="none" stroke="#fff" stroke-width="3"/><path d="M19 19l7 7" stroke="#fff" stroke-width="3"/></svg>
  <div class="tile" style="left:457px;top:1740px;background:linear-gradient(180deg,#8fb8de 0%,#c79a72 55%,#3a6a8a 100%)" role="img" aria-label="Harbour building with colourful boats in front"></div>
  <div class="tile" style="left:781px;top:1740px;background:linear-gradient(180deg,#b8d0e6 0%,#c07a6a 45%,#8a8a86 100%)" role="img" aria-label="Cobbled street lined with painted houses"></div>
  <div class="tile" style="left:132px;top:2028px;background:linear-gradient(180deg,#7fb0dc 0%,#d8c8b0 50%,#3a8a8a 100%)" role="img" aria-label="Stone bridge over a canal with a gondola"></div>
  <div class="tile" style="left:457px;top:2028px;background:linear-gradient(180deg,#4a7ab8 0%,#c8885a 50%,#2a4a6a 100%)" role="img" aria-label="Colourful old town rooftops beside the water"></div>
  <div class="tile" style="left:781px;top:2028px;background:linear-gradient(180deg,#3a7ad0 0%,#d8b83a 50%,#3a6a3a 100%)" role="img" aria-label="Colourful hilltop palace among trees"></div>
</section>

<section>
  <h2 class="abs heading" style="left:132px;top:2322px"><span class="lead">Our</span><span class="main">Membership</span></h2>
  <div class="member" style="left:132px"><span class="member-badge"></span></div>
  <div class="member" style="left:371px"><span class="member-badge"></span></div>
  <div class="member" style="left:610px"><span class="member-badge"></span></div>
  <div class="member" style="left:848px"><span class="member-badge"></span></div>
</section>

<footer>
  <div class="abs map" role="img" aria-label="Dark street map of the office area"></div>
  <div class="abs contact-card">
    <div><svg viewBox="0 0 18 18"><path d="M4 2c-2 2-1 6 3 10s8 5 10 3l-3-3-2 2c-2-1-4-3-5-5l2-2z" fill="#f39a2b"/></svg>0117-555-0142</div>
    <div><svg viewBox="0 0 18 18"><rect x="1" y="4" width="16" height="11" fill="#f39a2b"/><path d="M1 4l8 6 8-6" fill="none" stroke="#333" stroke-width="1.5"/></svg>info@thornwickestates.co.uk</div>
    <div><svg viewBox="0 0 18 18"><path d="M9 1a6 6 0 0 0-6 6c0 5 6 10 6 10s6-5 6-10a6 6 0 0 0-6-6z" fill="#f39a2b"/><circle cx="9" cy="7" r="2" fill="#333"/></svg>12 Fennel Rd old market bristol,BS2</div>
  </div>
  <svg class="abs" style="left:611px;top:2808px" width="20" height="30" viewBox="0 0 20 30"><path d="M10 0a9 9 0 0 0-9 9c0 8 9 21 9 21s9-13 9-21a9 9 0 0 0-9-9z" fill="#c0392b"/><circle cx="10" cy="9" r="3" fill="#7a1f16"/></svg>
  <div class="abs bottom"></div>
  <p class="abs copyright">© 2016 Thornwick estates, All rights reserved.</p>
  <div class="abs social"><span></span><span></span><span></span><span></span></div>
</footer>

</body>
</html>
```